Letterhead for 3 attorney Workers' Comp law firm

We are a 3 attorney law office. We specialize in Workers' Compensation. Our office represents workers who are injured on the job, and the estates of workers who are killed one the job.
When we started our office, we created our own letterhead & have been using it for years. We've just recently hired the 3rd attorney, and were going to just add his name to the letterhead, but have decided we wanted to get a professionally designed letterhead and business cards at this point.
We want something that looks clean and professional. It must look good in black and white because we often make multiple copies of our documents. We're hoping for a design that resonates confidence, reliability and experience.
The design must include the firm name: Thornbury & Calder, PLLC. We would like the PLLC to be small compared to the Thornbury & Calder graphic. We also want to incorporate the attorney names: Ivar Thornbury, Delia Calder, and Glen Rutledge. Our current letterhead has our contact info in the footer at the bottom of the page. We like that design, but are open to the idea of having it at the top. We'll leave that at the discretion of the designer. Our contact info is as follows: 482 S. Harrow Avenue, Suite 310 Bellingham, WA 98417 Phone: 360-555-2917, Fax: 360-555-4068, and our website: www.thornburycalder.example
Target Market(s)
Clients, courts, other legal offices, doctors offices. These are the people who see our letterhead most frequently. It's not so much for marketing purposes, mainly so that we have a professional image when sending out documents.
Industry/Entity Type
Law Firm
Contact Information for Business Card
On the back of the business card: it can be designed, or be a template for filling in appointment reminder information (i.e. date, time, etc)
Colors
Designer to choose colors to be used in the design.
Requirements
Must have
- Must have our firm name at the top.
- Must include the attorney names.
- Must have all of our contact information (can be at top or bottom - whatever looks best with the design)
Nice to have
- A strong, confident design
Should not have
- We don't want the design to be playful, cartoony or busy.

```html
<!DOCTYPE html>
<html lang="en">
<head>
<meta charset="utf-8">
<title>Thornbury &amp; Calder, PLLC — Stationery</title>
<link rel="stylesheet" href="https://fonts.googleapis.com/css2?family=Arimo:wght@400&display=swap">
<style>
  :root {
    --backdrop: #ececec;
    --paper: #ffffff;
    --ink: #111111;
    --ink-soft: #333333;
    --edge: #d6d6d6;
  }
  * { margin: 0; padding: 0; box-sizing: border-box; }
  html, body { width: 1200px; height: 1200px; overflow: hidden; }
  body {
    background: var(--backdrop);
    font-family: "Arimo", Arial, sans-serif;
    color: var(--ink);
    position: relative;
  }
  .sheet {
    position: absolute;
    background: var(--paper);
    border: 1px solid var(--edge);
  }

  /* Letterhead */
  .letterhead { left: 218px; top: 342px; width: 233px; height: 507px; }
  .letterhead .firm-mark { position: absolute; left: 118px; top: 15px; width: 108px; }
  .letterhead .firm-name { font-size: 10px; line-height: 1.1; }
  .letterhead .firm-pllc { font-size: 4px; }
  .letterhead .firm-partners { font-size: 3.6px; line-height: 1.25; color: var(--ink-soft); margin-top: 1px; }
  .letterhead .contact {
    position: absolute; right: 7px; top: 45px;
    font-size: 4px; line-height: 6.5px; text-align: right; list-style: none;
  }
  .letterhead .contact li { display: flex; justify-content: flex-end; align-items: center; gap: 2px; }
  .letterhead .contact svg { width: 5px; height: 5px; }
  .letterhead .site {
    position: absolute; bottom: 30px; left: 0; right: 0;
    text-align: center; font-size: 6px; letter-spacing: 0.5px;
  }

  /* Cards */
  .card { width: 333px; height: 201px; left: 657px; }
  .card-front { top: 363px; }
  .card-back { top: 618px; }

  .firm-mark .firm-name-row { display: flex; align-items: flex-end; justify-content: space-between; }
  .firm-rule { border-bottom: 1px solid var(--ink); margin-top: 1px; }

  .card-front .firm-mark { position: absolute; left: 63px; top: 34px; width: 195px; }
  .card-front .firm-name { font-size: 19px; line-height: 1.1; }
  .card-front .firm-pllc { font-size: 7px; }
  .card-front .firm-partners { font-size: 7px; line-height: 1.25; color: var(--ink-soft); margin-top: 2px; }
  .card-front .divider {
    position: absolute; left: 27px; right: 27px; top: 100px;
    border-top: 1.5px solid var(--ink);
  }
  .card-front .contact {
    position: absolute; left: 84px; top: 117px; list-style: none;
    font-size: 8px; line-height: 11px;
  }
  .card-front .contact li { display: flex; align-items: flex-start; gap: 5px; }
  .card-front .contact svg { width: 8px; height: 8px; margin-top: 1.5px; flex: none; }

  .card-back .firm-mark { position: absolute; left: 42px; top: 67px; width: 254px; }
  .card-back .firm-name { font-size: 25px; line-height: 1.1; }
  .card-back .firm-pllc { font-size: 8px; }
  .card-back .firm-partners { font-size: 8px; line-height: 1.25; color: var(--ink-soft); margin-top: 2px; }
  .card-back .site {
    position: absolute; bottom: 18px; left: 0; right: 0;
    text-align: center; font-size: 10px; letter-spacing: 1px;
  }
</style>
</head>
<body>

<svg width="0" height="0" style="position:absolute">
  <defs>
    <symbol id="icon-pin" viewBox="0 0 10 10"><circle cx="5" cy="5" r="5" fill="#111"/><path d="M5 2.2a1.9 1.9 0 0 0-1.9 1.9C3.1 5.6 5 7.8 5 7.8s1.9-2.2 1.9-3.7A1.9 1.9 0 0 0 5 2.2z" fill="#fff"/></symbol>
    <symbol id="icon-phone" viewBox="0 0 10 10"><circle cx="5" cy="5" r="5" fill="#111"/><path d="M3.3 2.6l1 1.1-.5.7c.3.7.9 1.3 1.6 1.6l.7-.5 1.1 1-.6.9C4.8 7.3 2.7 5.2 2.6 3.2z" fill="#fff"/></symbol>
    <symbol id="icon-fax" viewBox="0 0 10 10"><circle cx="5" cy="5" r="5" fill="#111"/><rect x="2.8" y="4" width="4.4" height="2.6" fill="#fff"/><rect x="3.6" y="2.6" width="2.8" height="1.2" fill="#fff"/></symbol>
    <symbol id="icon-web" viewBox="0 0 10 10"><circle cx="5" cy="5" r="5" fill="#111"/><circle cx="5" cy="5" r="2.6" fill="none" stroke="#fff" stroke-width=".7"/><path d="M2.4 5h5.2M5 2.4v5.2" stroke="#fff" stroke-width=".6"/></symbol>
  </defs>
</svg>

<section class="sheet letterhead" aria-label="Letterhead">
  <header class="firm-mark">
    <div class="firm-name-row"><span class="firm-name">Thornbury &amp; Calder</span><span class="firm-pllc">PLLC</span></div>
    <div class="firm-rule"></div>
    <p class="firm-partners">Ivar Thornbury, Delia Calder<br>&amp; Glen Rutledge Attorneys</p>
  </header>
  <ul class="contact">
    <li>482 S. Harrow Avenue <svg><use href="#icon-pin"/></svg></li>
    <li>Suite 310 Bellingham, WA 98417 &nbsp;&nbsp;&nbsp;</li>
    <li>360-555-2917 <svg><use href="#icon-phone"/></svg></li>
    <li>360-555-4068 <svg><use href="#icon-fax"/></svg></li>
  </ul>
  <footer class="site">www.thornburycalder.example</footer>
</section>

<section class="sheet card card-front" aria-label="Business card front">
  <header class="firm-mark">
    <div class="firm-name-row"><span class="firm-name">Thornbury &amp; Calder</span><span class="firm-pllc">PLLC</span></div>
    <div class="firm-rule"></div>
    <p class="firm-partners">Ivar Thornbury, Delia Calder<br>&amp; Glen Rutledge Attorneys</p>
  </header>
  <div class="divider"></div>
  <ul class="contact">
    <li><svg><use href="#icon-pin"/></svg><span>482 S. Harrow Avenue<br>Suite 310 Bellingham, WA 98417</span></li>
    <li><svg><use href="#icon-phone"/></svg><span>360-555-2917</span></li>
    <li><svg><use href="#icon-fax"/></svg><span>360-555-4068</span></li>
    <li><svg><use href="#icon-web"/></svg><span>www.thornburycalder.example</span></li>
  </ul>
</section>

<section class="sheet card card-back" aria-label="Business card back">
  <header class="firm-mark">
    <div class="firm-name-row"><span class="firm-name">Thornbury &amp; Calder</span><span class="firm-pllc">PLLC</span></div>
    <div class="firm-rule"></div>
    <p class="firm-partners">Ivar Thornbury, Delia Calder<br>&amp; Glen Rutledge Attorneys</p>
  </header>
  <footer class="site">www.thornburycalder.example</footer>
</section>

</body>
</html>
```